Brochure for a six month Life Transformation program for executives

I need a A4 brochure that will be physically printed out to give to prospective clients for a six month coaching, life transformation program. I have included here a video link that discusses the brief in detail.
https://www.clipvane.com/view/4a81f0c2d9e347b6a05c1e7d92b8f3a6

I've uploaded a file with logos and photos to include as well as a outline of each page.
Updates

Here is an updated video to show you what I'm liking what I don't like https://www.clipvane.com/view/9e2d47b1a6f04c38b5d1f7a3c08e6b24

Target Market(s)

35 - 55 male executives

Industry/Entity Type

Life Coaching

Requirements
Must have
• All the information in the outline
Nice to have
• icons, vector diagrams, the theme of transformation and revolution

```html
<!DOCTYPE html>
<html lang="en">
<head>
<meta charset="utf-8">
<title>Keystone Shift – Brochure</title>
<link href="https://fonts.googleapis.com/css2?family=Montserrat:wght@400;600;700;800&family=Russo+One&display=swap" rel="stylesheet">
<style>
  :root{
    --blue:#1c4597;
    --blue-deep:#173a80;
    --ink:#333a48;
    --muted:#6b7280;
    --paper:#ffffff;
    --paper-soft:#f3f4f6;
    --stage-light:#dcdcdc;
    --stage-mid:#b6b7b9;
    --turf:#7fae4a;
    --turf-dark:#4f8a2e;
    --haze:#c9ccd1;
  }
  *{box-sizing:border-box;margin:0;padding:0}
  html,body{width:1200px;height:2458px;overflow:hidden}
  body{font-family:"Montserrat",sans-serif;color:var(--ink);background:var(--stage-light)}
  .stage{height:819.33px;display:flex;align-items:center;justify-content:center}
  .stage--mid{background:var(--stage-mid)}
  .page{position:relative;width:550px;height:778px;background:var(--paper);overflow:hidden;box-shadow:0 6px 18px rgba(0,0,0,.18)}
  .spread{display:flex;box-shadow:0 8px 22px rgba(0,0,0,.2)}
  .spread .page{box-shadow:none}
  .abs{position:absolute}
  .photo{position:absolute;background:linear-gradient(180deg,var(--haze) 0%,#dfe2e6 35%,#a9c98a 62%,var(--turf) 80%,var(--turf-dark) 100%)}
  .brand{display:flex;align-items:center;gap:8px;font-family:"Montserrat",sans-serif;font-weight:700;font-size:11px;letter-spacing:2.5px;text-transform:uppercase;color:var(--blue)}
  .brand__mark{width:12px;height:12px;background:var(--blue)}
  .logo-box{position:absolute;background:var(--paper);display:flex;align-items:center;justify-content:center}
  .headline{position:absolute;font-family:"Russo One",sans-serif;text-transform:uppercase;line-height:1}
  .headline__top{color:var(--blue);font-size:31px}
  .headline__band{display:inline-block;margin-top:6px;background:var(--blue);color:#fff;font-size:34px;padding:6px 22px 6px 26px;clip-path:polygon(4% 0,100% 0,96% 100%,0 100%)}
  .url{position:absolute;font-size:12px;color:var(--muted);letter-spacing:.5px}
  .url b{color:var(--ink);font-weight:700}
  /* back cover */
  .back__intro{position:absolute;left:38px;top:96px;width:350px;color:#fff;font-size:14px;line-height:1.45;letter-spacing:.3px}
  .back__foot{position:absolute;left:0;right:0;bottom:64px;display:flex;align-items:center;justify-content:center;gap:26px}
  .back__divider{width:1px;height:40px;background:#c4c8d0}
  .contact__phone{display:flex;align-items:center;gap:8px;font-weight:800;font-size:20px;color:var(--ink)}
  .contact__web{font-size:10px;color:var(--muted);margin-top:3px;padding-left:24px}
  /* inner left */
  .creds{position:absolute;right:0;top:0;bottom:0;width:300px;background:linear-gradient(90deg,rgba(255,255,255,.55),rgba(255,255,255,.96) 22%);padding:70px 26px 0 42px}
  .cred{display:flex;gap:10px;align-items:flex-start;margin-bottom:22px}
  .cred__text{font-weight:700;font-size:11.5px;line-height:1.3;color:var(--ink)}
  .tick{flex:none;width:16px;height:16px;margin-top:1px}
  .badges{display:grid;grid-template-columns:repeat(2,70px);gap:12px 18px;margin:-6px 0 24px 26px}
  .badge{height:26px;border-radius:3px}
  .badge--red{background:#d8322c}
  .badge--dark{background:#2b2f38}
  .badge--green{background:#7cb342}
  .badge--grey{background:#c9ccd1;border-radius:13px}
  .page-no{position:absolute;bottom:36px;font-size:10px;color:var(--blue)}
  .page-no b{font-weight:800}
  /* inner right */
  .col{position:absolute;width:215px;font-size:8.6px;line-height:1.5;color:var(--ink)}
  .h2{font-size:15px;line-height:1.15;text-transform:uppercase;color:var(--blue);font-weight:800;margin-bottom:7px}
  .h2 span{font-weight:400;color:var(--ink)}
  .col p{margin-bottom:9px}
  .signature{width:120px;height:30px;margin:2px 0 14px;border-bottom:1px solid #c4c8d0}
  .quote-band{position:absolute;left:0;right:0;top:560px;height:150px;background:var(--blue)}
  .quote{position:absolute;color:#fff;font-size:9.5px;line-height:1.45}
  .quote__mark{display:inline-block;background:#fff;color:var(--blue);font-family:"Russo One",sans-serif;font-size:20px;line-height:20px;width:26px;height:22px;text-align:center;margin-bottom:8px}
  .quote cite{display:block;font-style:normal;font-weight:700;margin-top:6px}
  .quote-divider{position:absolute;top:582px;left:282px;width:1px;height:105px;background:rgba(255,255,255,.45)}
  .rule{position:absolute;height:1px;background:#c4c8d0}
</style>
</head>
<body>

<!-- Front cover -->
<section class="stage">
  <article class="page cover">
    <div class="photo" style="left:0;top:60px;width:550px;height:520px;border-bottom-left-radius:50% 60px;border-bottom-right-radius:50% 60px" role="img" aria-label="Photo of a coach in a cap sitting on a sports field, stretching"></div>
    <svg class="abs" style="left:0;top:0" width="550" height="120" viewBox="0 0 550 120">
      <polygon points="0,0 550,0 550,22 0,110" fill="var(--blue)"/>
      <polygon points="390,60 550,26 550,40 390,74" fill="var(--blue)"/>
    </svg>
    <div class="logo-box" style="left:230px;top:22px;width:170px;height:92px"><div class="brand"><span class="brand__mark"></span>Keystone Shift</div></div>
    <div class="headline" style="left:58px;top:596px">
      <div class="headline__top">Your life, your potential,</div>
      <div class="headline__band">Your revolution</div>
    </div>
    <div class="url" style="left:250px;top:700px">www.<b>KeystoneShift</b>.com</div>
  </article>
</section>

<!-- Back and front cover -->
<section class="stage stage--mid">
  <div class="spread">
    <article class="page back">
      <div class="photo" style="left:0;top:150px;width:550px;height:490px;background:linear-gradient(180deg,#d9dce0 0%,#c3c8cc 30%,#8fbb5d 55%,var(--turf) 75%,var(--turf-dark) 100%)" role="img" aria-label="Photo of the coach stretching his leg on a running track"></div>
      <svg class="abs" style="left:0;top:0" width="550" height="778" viewBox="0 0 550 778">
        <polygon points="0,0 550,0 550,150 0,250" fill="var(--blue)"/>
        <polygon points="0,262 550,162 550,170 0,270" fill="var(--blue)"/>
        <path d="M0,640 L550,560 L550,778 L0,778 Z" fill="var(--paper)"/>
        <polygon points="0,700 550,610 550,618 0,708" fill="var(--blue)"/>
      </svg>
      <p class="back__intro">A six month life transformation program for overworked executives to restore life balance through health and fitness optimization while maintaining their high performance.</p>
      <div class="back__foot">
        <div class="brand"><span class="brand__mark"></span>Keystone Shift</div>
        <div class="back__divider"></div>
        <div class="contact">
          <div class="contact__phone">
            <svg width="16" height="16" viewBox="0 0 24 24"><path fill="var(--blue)" d="M6.6 10.8a15.1 15.1 0 0 0 6.6 6.6l2.2-2.2a1 1 0 0 1 1-.25 11.4 11.4 0 0 0 3.6.57 1 1 0 0 1 1 1V20a1 1 0 0 1-1 1A17 17 0 0 1 3 4a1 1 0 0 1 1-1h3.5a1 1 0 0 1 1 1c0 1.25.2 2.45.57 3.57a1 1 0 0 1-.25 1z"/></svg>
            555 014 2677
          </div>
          <div class="contact__web">www.KeystoneShift.com</div>
        </div>
      </div>
    </article>
    <article class="page cover">
      <div class="photo" style="left:0;top:60px;width:550px;height:520px;border-bottom-left-radius:50% 60px;border-bottom-right-radius:50% 60px" role="img" aria-label="Photo of a coach in a cap sitting on a sports field, stretching"></div>
      <svg class="abs" style="left:0;top:0" width="550" height="120" viewBox="0 0 550 120">
        <polygon points="0,0 550,0 550,22 0,110" fill="var(--blue)"/>
        <polygon points="390,60 550,26 550,40 390,74" fill="var(--blue)"/>
      </svg>
      <div class="logo-box" style="left:230px;top:22px;width:170px;height:92px"><div class="brand"><span class="brand__mark"></span>Keystone Shift</div></div>
      <div class="headline" style="left:58px;top:596px">
        <div class="headline__top">Your life, your potential,</div>
        <div class="headline__band">Your revolution</div>
      </div>
      <div class="url" style="left:250px;top:700px">www.<b>KeystoneShift</b>.com</div>
    </article>
  </div>
</section>

<!-- Inner spread -->
<section class="stage">
  <div class="spread">
    <article class="page inner-left">
      <div class="photo" style="left:0;top:0;width:550px;height:778px;background:linear-gradient(180deg,#bfc4ca 0%,#d6d9dd 40%,#9cc46c 70%,var(--turf) 85%,var(--turf-dark) 100%)" role="img" aria-label="Photo of the coach in a purple top kneeling on a sports field"></div>
      <div class="creds">
        <div class="cred"><svg class="tick" viewBox="0 0 16 16"><circle cx="8" cy="8" r="7" fill="none" stroke="var(--ink)" stroke-width="1.4"/><path d="M4.5 8.2l2.3 2.3 4.7-4.8" fill="none" stroke="var(--ink)" stroke-width="1.6"/></svg><p class="cred__text">Internationally educated with multiple qualifications from Australia and Canada</p></div>
        <div class="badges" aria-label="Certification badges">
          <div class="badge badge--red"></div><div class="badge badge--dark"></div>
          <div class="badge badge--green"></div><div class="badge badge--grey"></div>
        </div>
        <div class="cred"><svg class="tick" viewBox="0 0 16 16"><circle cx="8" cy="8" r="7" fill="none" stroke="var(--ink)" stroke-width="1.4"/><path d="M4.5 8.2l2.3 2.3 4.7-4.8" fill="none" stroke="var(--ink)" stroke-width="1.6"/></svg><p class="cred__text">Over 15 years experience, working directly with 100s of clients and facilitated well over 1000 fitness classes</p></div>
        <div class="cred"><svg class="tick" viewBox="0 0 16 16"><circle cx="8" cy="8" r="7" fill="none" stroke="var(--ink)" stroke-width="1.4"/><path d="M4.5 8.2l2.3 2.3 4.7-4.8" fill="none" stroke="var(--ink)" stroke-width="1.6"/></svg><p class="cred__text">We work with executives clients from companies like Norvale Foods, Harbor Media, Ventic, Orchard Labs</p></div>
        <div class="cred"><svg class="tick" viewBox="0 0 16 16"><circle cx="8" cy="8" r="7" fill="none" stroke="var(--ink)" stroke-width="1.4"/><path d="M4.5 8.2l2.3 2.3 4.7-4.8" fill="none" stroke="var(--ink)" stroke-width="1.6"/></svg><p class="cred__text">In 2016 selected to represent Toronto as an Elite Trainer to provide coaching services for Worldwide Prime Coach Network</p></div>
        <div class="cred"><svg class="tick" viewBox="0 0 16 16"><circle cx="8" cy="8" r="7" fill="none" stroke="var(--ink)" stroke-width="1.4"/><path d="M4.5 8.2l2.3 2.3 4.7-4.8" fill="none" stroke="var(--ink)" stroke-width="1.6"/></svg><p class="cred__text">Featured on CityPulse, Metro Daily, Trailhead Magazine</p></div>
        <div class="rule" style="left:42px;right:26px;bottom:66px"></div>
        <p class="page-no" style="right:26px">page <b>01</b></p>
      </div>
      <div class="brand abs" style="left:36px;bottom:40px;color:#fff"><span class="brand__mark" style="background:#fff"></span>Keystone Shift</div>
    </article>
    <article class="page inner-right">
      <div class="col" style="left:38px;top:58px">
        <h2 class="h2">What is a Keystone <span>Shift?</span></h2>
        <p>A Keystone Shift is to overthrow your old regimes and bad habits and become your true potential self, a version that is fit, healthy, confident and successful.</p>
        <div class="signature" role="img" aria-label="Handwritten signature of Dale Renner, founder"></div>
        <h2 class="h2">The program <span>in brief</span></h2>
        <p>A six month life transformation program for overworked executives to restore life balance through health and fitness optimization while maintaining their high functioning career. A combination of 1:1 coaching, workshops, live events, workouts and accountability groups creates a unique learning environment and an immersive experience for our clients to experience a Keystone Shift.</p>
        <p>We envision a world where people move past focusing on financial gains at the cost of their physical and mental health. One where all aspects of their life are truly balanced and they gain fulfilment through living a healthy, fit and confident life.</p>
      </div>
      <div class="col" style="left:296px;top:58px">
        <h2 class="h2">Who <span>it's for</span></h2>
        <p>High performing individuals who have focused on their career and other aspects of their life while neglecting their health and fitness. Executives and Business Leaders who want to optimise their life through enhancing their health and fitness.</p>
        <p>Self Employed Entrepreneurs who understand in order to achieve your potential you need accountability and a community of like minded people.</p>
        <p>Peak Physical Performance: be pain free and functionally fit. Physical confidence: we get you to not only look good, feel good, but love what you see in the mirror. Be in control of all aspects of your life, professionally and personally.</p>
      </div>
      <div class="quote-band"></div>
      <div class="quote" style="left:38px;top:580px;width:220px"><span class="quote__mark">“</span><br>No citizen has a right to be an amateur in the matter of physical training. What a disgrace it is for a man to grow old without ever seeing the beauty and strength of which his body is capable.<cite>- Theron of Argos</cite></div>
      <div class="quote-divider"></div>
      <div class="quote" style="left:300px;top:580px;width:210px"><span class="quote__mark">“</span><br>Take care of your body. It's the only place you have to live.<cite>— Walt Pemberton</cite></div>
      <div class="url" style="left:38px;top:732px;font-size:10px">www.<b>KeystoneShift</b>.com</div>
      <div class="rule" style="left:200px;right:90px;top:740px"></div>
      <p class="page-no" style="right:38px;bottom:31px">page <b>02</b></p>
    </article>
  </div>
</section>

</body>
</html>
```